Youth Sports Banner Ad - 3x5 ft banner special!

We are looking for a full page ad (8.5x11") to advertise our banner services for Youth Sports leagues. The flyers will be handed out to teams and parents in hopes to draw their business to us for team banners.
We want to show our logo, address (4187 Verbena Ln. Paso Robles). Please include that we are offering a youth sports special price on 3x5 ft team banners for $115 (plus tax). The pricing will include 1 layout with up to 2 revisions. We would like the ad to grab the attention of the audience and ask them to "Call, Email or Stop in Today!"

Our info that needs to be on the banner includes:
email: info@markwell47.net
phone: 805-291-6583

We want to really focus on our quick turnaround as we will be producing the banners withing 1-2 business days after artwork approval.
We would like to include the banner samples if possible, and if you see fit, also include that we would like the potential customer to email us their teams name, roster, and colors to help speed up the layout process.

Target Market(s)

Parents of kids playing youth sports. The flyer is meant to increase awareness of our sign shop, while offering a great discount on banners for youth sports banners.

Font styles to use
Sans Serif

Colors

Designer to choose colors to be used in the design.

Requirements
Must have
• Our logo, $115 plus tax banner price, our business information, request to send over all team information including name, roster, and team colors.
Nice to have
• Would like to see color in the ad! If you can tie in the Kelly green from our logo, that would be great.

```html
<!DOCTYPE html>
<html lang="en">
<head>
<meta charset="utf-8">
<title>Markwell Signs – Youth Sports Banner Special</title>
<link href="https://fonts.googleapis.com/css2?family=Oswald:wght@400;500;600;700&family=Roboto+Condensed:wght@400;700&family=Roboto:wght@300;400&family=Montserrat:wght@800;900&display=swap" rel="stylesheet">
<style>
  :root{
    --kelly:#0a9a4e;
    --ink:#111111;
    --grey:#555555;
    --team-purple:#2d2b86;
    --team-purple-light:#3d3aa0;
    --white:#ffffff;
    --card-border:#6d6d6d;
  }
  *{box-sizing:border-box;margin:0;padding:0}
  html,body{width:962px;height:1200px;overflow:hidden;background:#fff}
  .flyer{position:relative;width:962px;height:1200px;background:var(--white);font-family:'Roboto',sans-serif;color:var(--ink)}

  .brand{position:absolute;left:60px;top:52px;font-family:'Oswald',sans-serif;font-weight:700;color:var(--kelly);font-size:58px;line-height:0.95;text-transform:uppercase}
  .brand-mark{display:inline-block;width:22px;height:22px;background:var(--kelly);margin-right:10px;vertical-align:middle}

  .address{position:absolute;right:62px;top:64px;text-align:right;font-family:'Roboto',sans-serif;font-weight:300;font-size:26px;line-height:33px;color:var(--grey)}
  .social{position:absolute;right:62px;top:136px;display:flex;gap:14px}
  .social span{width:34px;height:34px;border:1.5px solid var(--grey);border-radius:50%}

  .team-banner{position:absolute;left:0;top:226px;width:962px;height:488px;overflow:hidden;
    background:repeating-conic-gradient(from 0deg at 50% 45%, var(--team-purple) 0deg 7deg, var(--team-purple-light) 7deg 14deg)}
  .mascot{position:absolute;left:300px;top:50px;width:360px;height:330px;border-radius:45% 45% 40% 40%;background:radial-gradient(circle,#d9d9e6 0%,#8c8cae 55%,#2d2b86 100%);opacity:.8}
  .roster{position:absolute;top:36px;font-family:'Montserrat',sans-serif;font-weight:900;font-size:36px;line-height:74.5px;color:var(--white);text-transform:uppercase;white-space:nowrap;
    text-shadow:-2px -2px 0 #000,2px -2px 0 #000,-2px 2px 0 #000,2px 2px 0 #000,3px 4px 2px rgba(0,0,0,.6)}
  .roster.left{left:26px}
  .roster.right{right:22px;text-align:right}
  .roster .num{font-size:32px;vertical-align:top}

  .offer{position:absolute;left:104px;top:126px;width:754px;height:256px;background:rgba(255,255,255,.9);border:3px solid var(--kelly);border-radius:12px;text-align:center}
  .offer-kicker{font-family:'Oswald',sans-serif;font-weight:600;font-size:54px;line-height:1;margin-top:36px;color:var(--ink);text-transform:uppercase;letter-spacing:-.5px;white-space:nowrap}
  .offer-price{font-family:'Oswald',sans-serif;font-weight:600;font-size:60px;line-height:1;margin-top:10px;color:var(--kelly);letter-spacing:-.5px;white-space:nowrap}
  .offer-price sup{font-size:18px;color:var(--ink);vertical-align:top;position:relative;top:8px;margin-left:2px}
  .offer-note{font-family:'Roboto Condensed',sans-serif;font-size:24px;margin-top:20px;color:var(--ink)}

  .credits{position:absolute;left:0;top:714px;width:962px;height:60px;background:#000;color:var(--white);font-family:'Montserrat',sans-serif;font-weight:800;font-size:27px;line-height:52px;text-transform:uppercase;display:flex;justify-content:space-between;padding:0 30px 0 28px;white-space:nowrap}

  .features{position:absolute;left:74px;top:746px;display:flex;gap:21px}
  .feature{width:255px;height:146px;background:var(--white);border:2px solid var(--card-border);border-radius:16px;text-align:center;padding:20px 14px 0}
  .feature h3{font-family:'Oswald',sans-serif;font-weight:500;font-size:23px;color:var(--kelly);text-transform:uppercase;line-height:1.1;letter-spacing:-.3px;white-space:nowrap}
  .feature p{font-family:'Roboto Condensed',sans-serif;font-size:16px;line-height:19px;margin-top:12px;color:var(--ink)}

  .cta-lead{position:absolute;left:0;width:962px;top:938px;text-align:center;font-family:'Roboto',sans-serif;font-weight:300;font-size:37px;color:var(--grey)}
  .cta-phone{position:absolute;left:0;width:962px;top:994px;text-align:center;font-family:'Oswald',sans-serif;font-weight:700;font-size:76px;line-height:1;letter-spacing:5px;color:var(--ink)}
  .cta-contact{position:absolute;left:0;width:962px;top:1088px;text-align:center;font-family:'Roboto Condensed',sans-serif;font-size:17px;color:var(--ink)}
  .cta-rule{position:absolute;left:238px;width:486px;top:1117px;height:2px;background:var(--ink)}
  .cta-tip{position:absolute;left:0;width:962px;top:1128px;text-align:center;font-family:'Roboto Condensed',sans-serif;font-size:17px;color:var(--ink)}
</style>
</head>
<body>
<div class="flyer">
  <div class="brand"><span class="brand-mark"></span>Markwell<br>Signs</div>

  <div class="address">4187 Verbena Ln.<br>Paso Robles, CA 93446</div>
  <div class="social"><span></span><span></span></div>

  <section class="team-banner">
    <div class="mascot" role="img" aria-label="Team mascot illustration"></div>
    <div class="roster left">
      <div><span class="num">#9</span> Benjamin</div>
      <div><span class="num">#5</span> Blane</div>
      <div><span class="num">#4</span> Kaden</div>
      <div><span class="num">#6</span> Cash</div>
      <div><span class="num">#2</span> Tristan</div>
      <div><span class="num">#7</span> Fernando</div>
    </div>
    <div class="roster right">
      <div><span class="num">#11</span> Maddox</div>
      <div><span class="num">#10</span> Kasen</div>
      <div><span class="num">#3</span> Isaac</div>
      <div><span class="num">#12</span> Ricky</div>
      <div><span class="num">#8</span> Travis</div>
      <div><span class="num">#13</span> Lazarus</div>
    </div>
    <div class="offer">
      <div class="offer-kicker">Youth Sports Special Price</div>
      <div class="offer-price">3x5 ft TEAM BANNERS $115<sup>+TAX</sup></div>
      <div class="offer-note">Includes 1 Layout With Up To 2 Revisions</div>
    </div>
  </section>

  <div class="credits"><span>Head Coach Renner</span><span>Sponsored by Dalbecks</span></div>

  <div class="features">
    <div class="feature"><h3>High Quality</h3><p>We make full color signs and banners utilizing top-of-the-line equipment and materials!</p></div>
    <div class="feature"><h3>Quick Turnaround</h3><p>Banners are produced 1-2 business days after artwork approval</p></div>
    <div class="feature"><h3>Low Cost</h3><p>Need a sign or banner that won't break the bank? We meet your needs!</p></div>
  </div>

  <div class="cta-lead">So What are You Waiting For?</div>
  <div class="cta-phone">805-291-6583</div>
  <div class="cta-contact">Call, Email or Stop in Today! - info@markwell47.net - www.markwell47.net</div>
  <div class="cta-rule"></div>
  <div class="cta-tip">Speed up process: Email us teams name, roster, and color.</div>
</div>
</body>
</html>
```